KPT Building And Maintenance

Need a very professional looking double sided Buisiness card with all my details phone number, name, email, license number.

Target Market(s)

construction industry

Industry/Entity Type

building

Contact Information for Business Card

Name Dale Whitcombe. Email Address Info@KPTBuilding.example.au mobile number 0452918730 licence number 871406D. web site

```html
<!DOCTYPE html>
<html lang="en">
<head>
<meta charset="utf-8">
<title>KPT Building And Maintenance – Business Card</title>
<link href="https://fonts.googleapis.com/css2?family=Montserrat:wght@400;500;600;700;800&display=swap" rel="stylesheet">
<style>
  :root {
    --stage: #5b5b5b;
    --card: #ffffff;
    --ink: #262626;
    --blue: #059fe3;
    --white: #ffffff;
  }
  * { box-sizing: border-box; margin: 0; padding: 0; }
  html, body { width: 1200px; height: 853px; overflow: hidden; }
  body {
    background: var(--stage);
    font-family: "Montserrat", sans-serif;
    color: var(--ink);
    position: relative;
  }
  .card {
    position: absolute;
    width: 560px;
    height: 320px;
    background: var(--card);
    border-radius: 24px;
    overflow: hidden;
    box-shadow: 0 8px 22px rgba(0,0,0,.35);
  }
  .card--front { left: 28px; top: 110px; }
  .card--back  { left: 612px; top: 423px; }

  /* front */
  .brand-stack {
    position: absolute; left: 34px; top: 40px;
    font-weight: 800; color: var(--ink); line-height: 1;
  }
  .brand-stack .brand-top { font-size: 48px; letter-spacing: 1px; }
  .brand-stack .brand-bottom { font-size: 28px; letter-spacing: 1px; margin-top: 4px; }
  .license {
    position: absolute; left: 38px; top: 136px;
    color: var(--blue); font-weight: 600; font-size: 13px; line-height: 1.2;
  }
  .services {
    position: absolute; left: 38px; top: 178px; list-style: none;
    font-size: 14px; line-height: 17px;
  }
  .services li { display: flex; align-items: center; gap: 8px; white-space: nowrap; }
  .services li::before {
    content: ""; width: 6px; height: 6px; background: var(--blue); flex: none;
  }
  .person {
    position: absolute; left: 290px; top: 30px; line-height: 1;
  }
  .person .name { color: var(--blue); font-weight: 600; font-size: 25px; }
  .person .role { font-size: 22px; margin-top: 4px; }
  .address {
    position: absolute; left: 296px; top: 100px;
    font-size: 14px; line-height: 18px; font-style: normal;
  }
  .contacts { position: absolute; list-style: none; font-size: 14px; line-height: 20px; }
  .card--front .contacts { left: 296px; top: 162px; }
  .contacts li { display: flex; align-items: center; gap: 9px; white-space: nowrap; }
  .contacts svg { width: 14px; height: 14px; flex: none; }
  .front-rule {
    position: absolute; left: 0; right: 0; top: 268px; height: 4px; background: var(--ink);
  }
  .front-band {
    position: absolute; left: 0; right: 0; top: 275px; bottom: 0; background: var(--blue);
  }

  /* back */
  .brand-line {
    position: absolute; left: 34px; top: 42px;
    font-weight: 800; font-size: 50px; letter-spacing: 1px; line-height: 1;
  }
  .title-line {
    position: absolute; left: 36px; top: 112px;
    font-size: 22px; line-height: 1; white-space: nowrap;
  }
  .title-line .name { color: var(--blue); font-weight: 600; }
  .title-line .divider { color: var(--blue); margin: 0 8px; }
  .title-line .role { font-weight: 600; }
  .card--back .address { left: 38px; top: 152px; font-size: 15px; line-height: 20px; }
  .card--back .contacts { left: 300px; top: 150px; }
  .back-base { position: absolute; left: 0; bottom: 0; width: 560px; height: 110px; }
  .back-band-text {
    position: absolute; left: 0; right: 0; bottom: 12px;
    color: var(--white); font-weight: 600; font-size: 12px; line-height: 18px;
    text-align: center;
  }
</style>
</head>
<body>

<section class="card card--front" aria-label="Business card front">
  <div class="brand-stack">
    <div class="brand-top">KPT</div>
    <div class="brand-bottom">BUILDING</div>
  </div>
  <p class="license">Licensed Number :<br>871406D</p>
  <ul class="services">
    <li>Installation</li>
    <li>24 Hour Repair</li>
    <li>Maintenance</li>
    <li>Safety &amp; Efficiency Plans</li>
  </ul>

  <div class="person">
    <div class="name">Dale Whitcombe</div>
    <div class="role">Owner</div>
  </div>
  <address class="address">Ironbark Road<br>56 Carver Street<br>Millbrook, 40517</address>
  <ul class="contacts">
    <li><svg viewBox="0 0 24 24"><path fill="var(--blue)" d="M6.6 10.8a15.1 15.1 0 0 0 6.6 6.6l2.2-2.2a1 1 0 0 1 1-.25 11.4 11.4 0 0 0 3.6.57 1 1 0 0 1 1 1V20a1 1 0 0 1-1 1A17 17 0 0 1 3 4a1 1 0 0 1 1-1h3.5a1 1 0 0 1 1 1c0 1.250.2 2.450.57 3.57a1 1 0 0 1-.25 1z"/></svg>0452918730</li>
    <li><svg viewBox="0 0 24 24"><rect x="2" y="5" width="20" height="14" rx="1" fill="var(--blue)"/><path d="M2 6l10 7 10-7" fill="none" stroke="#fff" stroke-width="2"/></svg>Info@KPTBuilding.example.au</li>
    <li><svg viewBox="0 0 24 24"><g fill="none" stroke="var(--blue)" stroke-width="2"><circle cx="12" cy="12" r="10"/><ellipse cx="12" cy="12" rx="4" ry="10"/><path d="M2 12h20M4 7h16M4 17h16"/></g></svg>KPTbuilding.example.au</li>
  </ul>
  <div class="front-rule"></div>
  <div class="front-band"></div>
</section>

<section class="card card--back" aria-label="Business card back">
  <div class="brand-line">KPT BUILDING</div>
  <div class="title-line"><span class="name">Dale Whitcombe</span><span class="divider">|</span><span class="role">Owner</span></div>
  <address class="address">56 Carver Street<br>Millbrook, 40517<br>Ironbark Road</address>
  <ul class="contacts">
    <li><svg viewBox="0 0 24 24"><path fill="var(--blue)" d="M6.6 10.8a15.1 15.1 0 0 0 6.6 6.6l2.2-2.2a1 1 0 0 1 1-.25 11.4 11.4 0 0 0 3.6.57 1 1 0 0 1 1 1V20a1 1 0 0 1-1 1A17 17 0 0 1 3 4a1 1 0 0 1 1-1h3.5a1 1 0 0 1 1 1c0 1.250.2 2.450.57 3.57a1 1 0 0 1-.25 1z"/></svg>0452918730</li>
    <li><svg viewBox="0 0 24 24"><rect x="2" y="5" width="20" height="14" rx="1" fill="var(--blue)"/><path d="M2 6l10 7 10-7" fill="none" stroke="#fff" stroke-width="2"/></svg>Info@KPTBuilding.example.au</li>
    <li><svg viewBox="0 0 24 24"><g fill="none" stroke="var(--blue)" stroke-width="2"><circle cx="12" cy="12" r="10"/><ellipse cx="12" cy="12" rx="4" ry="10"/><path d="M2 12h20M4 7h16M4 17h16"/></g></svg>KPTbuilding.example.au</li>
  </ul>
  <svg class="back-base" viewBox="0 0 560 110" preserveAspectRatio="none" aria-hidden="true">
    <polyline points="0,86 20,86 48,58 78,58 105,50 560,50" fill="none" stroke="var(--ink)" stroke-width="5"/>
    <rect x="0" y="58" width="560" height="52" fill="var(--blue)"/>
    <polygon points="0,90 22,90 50,62 80,62 107,58 0,58" fill="var(--card)"/>
  </svg>
  <p class="back-band-text">Licensed Number : 871406D<br>Installation · 24 Hour Repair · Maintenance · Safety &amp; Efficiency Plans</p>
</section>

</body>
</html>
```